Corvane Project Services - Flyer

Plotline Breif:
I need a single page A4 Capability Statement, which will be used to market our services to prospective clients, both in print and via email PDF.
It needs to look professional and should incorporate the elements I have uploaded into files, these include:
Capability Statement Text
Corvane Services Company Logo
Additional Logo’s (Tools We Use)
Glimmer Bay Pics can be cut into the page
I have included examples of capability statements as a guide to what i am looking for.
Regards
Derek
Engineering Consulting

```html
<!DOCTYPE html>
<html lang="en">
<head>
<meta charset="utf-8">
<title>Corvane Project Services – Capability Statement</title>
<link href="https://fonts.googleapis.com/css2?family=Montserrat:wght@600;700;800&family=Open+Sans:wght@400;600;700&display=swap" rel="stylesheet">
<style>
  :root{
    --stage:#a7a7a7;
    --paper:#ffffff;
    --navy:#1d2b4f;
    --ink:#333b48;
    --steel:#7fa6d6;
    --steel-dark:#5d87bf;
    --sky:#86c8ea;
    --panel:#e7e8ea;
    --bullet:#5d87bf;
  }
  *{box-sizing:border-box;margin:0;padding:0}
  html,body{width:1200px;height:906px;overflow:hidden;background:var(--stage)}
  .flyer{position:absolute;left:290px;top:18px;width:620px;height:870px;background:var(--paper);
    font-family:"Open Sans",Arial,sans-serif;color:var(--ink);overflow:hidden;box-shadow:0 6px 18px rgba(0,0,0,.25)}

  .brand{position:absolute;left:28px;top:40px;width:220px;display:flex;align-items:center;gap:10px}
  .brand-dot{width:46px;height:46px;border-radius:50%;background:var(--steel-dark);flex:none}
  .brand-name{font-family:"Montserrat",Arial,sans-serif;font-weight:700;color:var(--navy);font-size:15px;line-height:1.15;letter-spacing:.5px;text-transform:uppercase}

  .title-band{position:absolute;left:250px;top:18px;width:370px;height:140px;background:var(--steel);
    display:flex;align-items:center;padding-left:26px}
  .title-band h1{font-family:"Montserrat",Arial,sans-serif;font-weight:800;color:#fff;font-size:46px;line-height:1;letter-spacing:1px;text-transform:uppercase}

  .intro{position:absolute;left:250px;top:158px;width:370px;height:180px;background:var(--panel);padding:16px 22px 0 26px}
  .intro ul{list-style:none}
  .intro li{position:relative;padding-left:14px;font-size:9.6px;line-height:1.45;margin-bottom:6px}
  .intro li::before,.service-list li::before{content:"";position:absolute;left:0;top:4px;width:6px;height:6px;border:1.2px solid var(--bullet);border-radius:50%}

  .photo-desk{position:absolute;left:0;top:158px;width:360px;height:270px;
    background:linear-gradient(135deg,#e9eef4 0%,#cdd8e4 45%,#a9bccf 100%);
    clip-path:polygon(0 0,100% 0,100% 60%,78% 100%,0 100%)}
  .photo-desk.front{left:0;top:158px;width:250px;height:180px;clip-path:none;background:none}

  .gantt-shot{position:absolute;left:300px;top:338px;width:320px;height:190px;
    background:linear-gradient(160deg,#f4f6f9 0%,#dfe5ee 55%,#c9d3e0 100%);
    clip-path:polygon(14% 0,100% 0,100% 100%,0 100%)}

  .services{position:absolute;left:30px;top:452px;width:290px}
  .services-tag{display:inline-block;background:var(--steel);color:#fff;font-family:"Montserrat",Arial,sans-serif;
    font-weight:700;font-size:14px;padding:4px 12px;letter-spacing:.5px;text-transform:uppercase;margin-bottom:8px}
  .services h3{font-size:10.5px;font-weight:700;color:var(--navy);margin:6px 0 2px}
  .service-list{list-style:none}
  .service-list li{position:relative;padding-left:14px;font-size:9.6px;line-height:1.5}

  .tools{position:absolute;left:330px;top:560px;width:270px;height:160px;border:2px solid var(--steel);
    padding:16px 14px;display:grid;grid-template-columns:1fr 1fr;gap:10px 12px;align-content:center}
  .tool{font-family:"Open Sans",Arial,sans-serif;font-weight:700;font-size:12px;color:var(--navy);
    display:flex;align-items:center;gap:6px}
  .tool-mark{width:9px;height:9px;background:var(--steel-dark);flex:none}
  .tool.wide{grid-column:1 / span 2}

  .contact{position:absolute;left:0;top:742px;width:620px;text-align:center;color:var(--navy)}
  .contact .person{font-size:13px;font-weight:700;letter-spacing:.3px}
  .contact .person span{font-size:10px;font-weight:600}
  .contact .links{font-size:11px;font-weight:700;margin-top:3px}
  .contact .sep{margin:0 8px}

  .footer-band{position:absolute;left:0;bottom:0;width:620px;height:70px;background:var(--sky);
    display:flex;align-items:center;padding-left:30px}
  .phone{font-size:12px;font-weight:700;color:var(--navy)}
</style>
</head>
<body>
<article class="flyer">
  <div class="photo-desk" role="img" aria-label="Photo of colleagues reviewing printed reports and charts at a desk"></div>

  <header>
    <div class="brand">
      <span class="brand-dot"></span>
      <span class="brand-name">Corvane Project<br>Services</span>
    </div>
    <div class="title-band"><h1>Capability<br>Statement</h1></div>
  </header>

  <section class="intro">
    <ul>
      <li>Corvane Project Services Ltd. is a leading project control consultancy based in Co Westmere Ireland.</li>
      <li>For over 20 years we have been helping our clients to deliver complex projects and programs throughout mainland Europe.</li>
      <li>We are passionate about empower organisations to achieve their objectives, on time and on budget.</li>
      <li>We are continually innovating, evolving and learning, utilize the latest industry tools and techniques to deliver real value to our clients.</li>
      <li>Our goal is to make successful project delivery more achievable and repeatable.</li>
    </ul>
  </section>

  <div class="gantt-shot" role="img" aria-label="Screenshot of a project schedule Gantt chart"></div>

  <section class="services">
    <span class="services-tag">Core Services:</span>
    <h3>Planning and Scheduling</h3>
    <ul class="service-list">
      <li>Tender Planning</li>
      <li>Interactive Planning / Pull Planning</li>
      <li>EPCMV Planning &amp; Scheduling</li>
      <li>Schedule Earned Value Management</li>
      <li>Independent Schedule Quality Assessment</li>
      <li>Schedule Risk Analysis (Monte Carlo)</li>
      <li>Training</li>
    </ul>
    <h3>Management of Risk</h3>
    <ul class="service-list">
      <li>Risk Management Policies &amp; Procedures</li>
      <li>Risk Management Strategy</li>
      <li>Risk Registers</li>
      <li>Risk Improvement Planning</li>
      <li>Risk Response and Communication</li>
      <li>Risk Management Training</li>
    </ul>
    <h3>Cost Control:</h3>
    <ul class="service-list">
      <li>Estimating &amp; Forecasting</li>
      <li>Earned Value Analysis</li>
      <li>Progress Reporting</li>
      <li>Cost Risk Analysis</li>
    </ul>
  </section>

  <section class="tools" aria-label="Tools we use">
    <span class="tool"><span class="tool-mark"></span>Waypoint Pro</span>
    <span class="tool"><span class="tool-mark"></span>Quorra</span>
    <span class="tool"><span class="tool-mark"></span>Plotline</span>
    <span class="tool"><span class="tool-mark"></span>Cedarly</span>
    <span class="tool"><span class="tool-mark"></span>Keystone Planner</span>
    <span class="tool"><span class="tool-mark"></span>Riskframe</span>
    <span class="tool wide"><span class="tool-mark"></span>Brightspan Powerplan</span>
  </section>

  <section class="contact">
    <p class="person">DEREK HALLORAN <span>(Managing Director)</span></p>
    <p class="links">info@corvaneservices.ie<span class="sep">|</span>www.corvaneservices.ie</p>
  </section>

  <footer class="footer-band">
    <span class="phone">+353 (0)87 555 0142</span>
  </footer>
</article>
</body>
</html>
```